ALL TEXT Social Media Graphics

We are looking for a series of social media graphics for Instagram (new size: 4:5 (1080 x 1350 pixels) ratio that are ALL TEXT. We want the following quotes below on each graphic; one quote per graphic. AND, In very small letters at the bottom of each graphic, add @PaulaWrenLive
The look and feel of these graphics should be complimentary to the color palette attached below; but keep them simple. But the design is up to you; at the end of this document, I provided various samples of all text graphics that I like as examples.
The Quotes are in the attached WORD document
women trying to lose weight

```html
<!DOCTYPE html>
<html lang="en">
<head>
<meta charset="utf-8">
<title>Peach Season Reset – Text Posts</title>
<link href="https://fonts.googleapis.com/css2?family=Poppins:wght@500;600;700;800&display=swap" rel="stylesheet">
<style>
  :root {
    --board: #666666;
    --card: #ffffff;
    --ink: #111111;
    --accent: #b3135c;
  }
  * { margin: 0; padding: 0; box-sizing: border-box; }
  html, body { width: 1200px; height: 813px; overflow: hidden; background: var(--board); }
  .board { position: relative; width: 1200px; height: 813px; font-family: 'Poppins', sans-serif; }
  .post {
    position: absolute; width: 215px; height: 269px;
    background: var(--card);
    box-shadow: 0 1px 3px rgba(0,0,0,.25);
    padding: 42px 0 0 26px;
    white-space: nowrap;
  }
  .post--low { padding-top: 67px; }
  .row-1 { top: 101px; } .row-2 { top: 398px; }
  .col-1 { left: 46px; } .col-2 { left: 274px; } .col-3 { left: 497px; } .col-4 { left: 725px; } .col-5 { left: 950px; }
  .lead { font-weight: 700; font-size: 12.5px; line-height: 15.4px; color: var(--ink); letter-spacing: -0.1px; }
  .headline { margin-top: 20px; font-weight: 800; font-size: 17.8px; line-height: 20.2px; color: var(--accent); letter-spacing: -0.1px; }
  .cta { margin-top: 3px; font-weight: 600; font-size: 7.6px; line-height: 12.9px; color: var(--ink); text-transform: uppercase; }
  .cta--tight { line-height: 10.3px; }
  .cta .keyword { color: var(--accent); }
  .handle { position: absolute; left: 26px; top: 233px; font-weight: 600; font-size: 5.4px; color: var(--ink); text-transform: uppercase; letter-spacing: 0.1px; }
</style>
</head>
<body>
<main class="board">

  <article class="post row-1 col-1">
    <p class="lead">You’ve Got 8 Weeks And<br>The Perfect Plan To Drop<br>30 Pounds.</p>
    <h2 class="headline">Let’s Get<br>Snatched This<br>Summer With The<br>Peach Season<br>Reset.</h2>
    <p class="cta">Comment <span class="keyword">“Summer”</span>!</p>
    <p class="handle">@PaulaWrenLive</p>
  </article>

  <article class="post row-1 col-2">
    <p class="lead">Don’t Wait ’Til Next<br>Summer To Get Right. The<br>Time Is Now.</p>
    <h2 class="headline">Drop 30 Pounds<br>With The Peach<br>Season<br>Reset.</h2>
    <p class="cta">Comment <span class="keyword">“Summer”</span>!</p>
    <p class="handle">@PaulaWrenLive</p>
  </article>

  <article class="post row-1 col-3">
    <p class="lead">Sis, We’re Dropping Belly<br>Flat And Saying Goodbye<br>To Stubborn Pounds.</p>
    <h2 class="headline">Join The Peach<br>Season<br>Reset.</h2>
    <p class="cta">Comment <span class="keyword">“Summer”</span>!</p>
    <p class="handle">@PaulaWrenLive</p>
  </article>

  <article class="post row-1 col-4">
    <p class="lead">Nothing Feels Better Than<br>Seeing That Scale Drop<br>Week After Week.</p>
    <h2 class="headline">Let’s Lose Up To<br>30 Pounds This<br>Summer<br>Together.</h2>
    <p class="cta">Comment <span class="keyword">“Summer”</span> to join<br>the Peach Season Reset!!</p>
    <p class="handle">@PaulaWrenLive</p>
  </article>

  <article class="post row-1 col-5">
    <p class="lead">Snatched Waist,<br>Flat Tummy,<br>30 Pounds Lighter</p>
    <h2 class="headline">That’s What The<br>Peach Season<br>Reset<br>Challenge Delivers.</h2>
    <p class="cta">Comment <span class="keyword">“Peach”</span> to get the plan</p>
    <p class="handle">@PaulaWrenLive</p>
  </article>

  <article class="post row-2 col-1">
    <p class="lead">You Can Absolutely Be<br>Down 20–30 Pounds By<br>End Of Summer.</p>
    <h2 class="headline">All It Takes Is The<br>Right Plan And<br>You’ve Found It.</h2>
    <p class="cta cta--tight">Comment <span class="keyword">“Peach”</span> for the<br>Peach Season Reset!</p>
    <p class="handle">@PaulaWrenLive</p>
  </article>

  <article class="post row-2 col-2">
    <p class="lead">You Don’t Need Another<br>Diet You Need A System<br>That Works.</p>
    <h2 class="headline">Drop 30 Pounds<br>With The Peach<br>Season<br>Reset.</h2>
    <p class="cta">Comment <span class="keyword">“Summer”</span> to start now!</p>
    <p class="handle">@PaulaWrenLive</p>
  </article>

  <article class="post row-2 col-3">
    <p class="lead">This Summer Ain’t Over<br>And Neither Are Your<br>Body Goals.</p>
    <h2 class="headline">Drop 30 Pounds<br>With The Peach<br>Season<br>Reset.</h2>
    <p class="cta">Comment <span class="keyword">“Peach”</span> to get the plan!</p>
    <p class="handle">@PaulaWrenLive</p>
  </article>

  <article class="post post--low row-2 col-4">
    <p class="lead">If Your Goal Is A Tiny<br>Waist, Flat Belly, And 30<br>Pounds Down</p>
    <h2 class="headline">This Is The Plan.</h2>
    <p class="cta">Comment <span class="keyword">“Summer”</span> to join<br>the Peach Season Reset!!</p>
    <p class="handle">@PaulaWrenLive</p>
  </article>

  <article class="post row-2 col-5">
    <p class="lead">There’s Still Time To<br>Drop The 30 Pounds<br>And Slay This Summer.</p>
    <h2 class="headline">The Peach<br>Season<br>Reset Has<br>The Blueprint.</h2>
    <p class="cta">Comment <span class="keyword">“Peach”</span>!</p>
    <p class="handle">@PaulaWrenLive</p>
  </article>

</main>
</body>
</html>
```